依頼詳細
レスポンシブウェブデザインを意識したデザインでお願いします。
参考URL
https://morisato-koubou.jp/

デザインに関しては、添付してあるデザインレイアウトシートを基にお願いします。

まずはパソコンサイトのデザインをお願いします。
当選後、スマホデザインをお願いします。

既存のテンプレートを使う場合は
テンプレート名を下記のような記載を提案の中にいれてください。
例:WordpressテーマはKandoria、デザインスキンは無料のHLM2019 RX4(http://kandoria.com/ex_plugin/hlmnagoya2019_rx4/)をベースにデザインいたしました。
など

素材となる写真は現在、撮影中ですので、一旦他のサイトや参考URLの写真をサンプルとして入れてください。(サンプルなどの表記をお願いします)
また、購入が必要な写真などを利用した場合は、Pelmora Stock(https://stock.pelmora.com/jp/)からファイル番号と価格を教えてください。
ページ数
1ページ
希望イメージ
シンプル 複雑
単色 カラフル
暗い 明るい
日常 高級
遊び心 厳粛
未来的 伝統的
女性的 男性的
希望する色
茶系、緑系
納品ファイル
• イラストレーター形式 (.ai)
• フォトショップ形式 (.psd)
• PNG形式 (.png)
補足説明
上記のいずれか1つ。アウトラインありとなしの2つ。

クライアントのイメージ通りでした。

たくさんのご提案ありがとうございました。
次回もぜひ、よろしくお願い致します。

```html
<!DOCTYPE html>
<html lang="ja">
<head>
<meta charset="utf-8">
<title>株式会社モリサト</title>
<link rel="stylesheet" href="https://fonts.googleapis.com/css2?family=Noto+Sans+JP:wght@400;500;700&family=Noto+Serif+JP:wght@500;700&display=swap">
<style>
:root{
  --green:#1f8b3b;
  --green-dark:#15702e;
  --green-deep:#0f5f26;
  --brown:#c27a17;
  --beige:#f3efe6;
  --ink:#333;
  --muted:#777;
  --line:#ddd;
  --wood-a:#c9a277;
  --wood-b:#8a6440;
}
*{margin:0;padding:0;box-sizing:border-box}
html,body{width:1200px;height:3776px;overflow:hidden}
body{font-family:"Noto Sans JP",sans-serif;color:var(--ink);background:#fff;font-size:14px;line-height:1.6}
.photo{background:linear-gradient(135deg,var(--wood-a),var(--wood-b));position:relative;overflow:hidden}
.photo.light{background:linear-gradient(135deg,#e4cfa8,#b48a5c)}
.photo.grey{background:linear-gradient(135deg,#c8c3bb,#8d8780)}
.photo.green{background:linear-gradient(135deg,#9fb77a,#5f7d3e)}

/* header */
.site-header{height:88px;display:flex;align-items:center;justify-content:space-between;padding:0 60px}
.brand{display:flex;align-items:center;gap:12px;font-family:"Noto Serif JP",serif;font-weight:700;font-size:26px;color:var(--ink)}
.brand-mark{width:38px;height:38px;background:var(--green)}
.contact{text-align:right}
.contact-note{font-size:12px;color:var(--muted)}
.contact-tel{display:flex;align-items:center;gap:6px;justify-content:flex-end;font-size:28px;font-weight:700;color:var(--green);line-height:1.1}
.global-nav{height:40px;display:flex;justify-content:center;border-top:1px solid var(--line);border-bottom:1px solid var(--line)}
.global-nav a{padding:0 26px;line-height:38px;font-size:13px;color:var(--ink);text-decoration:none;border-right:1px solid var(--line)}
.global-nav a:first-child{border-left:1px solid var(--line)}
.global-nav a.cta{background:var(--green);color:#fff}
.hero{height:492px}

/* sections */
.section{padding-top:50px;overflow:hidden}
.section-title{font-family:"Noto Serif JP",serif;font-weight:500;font-size:34px;line-height:1.6;text-align:center;letter-spacing:.08em;padding-bottom:18px}
.section-title::after{content:"";display:block;width:60px;height:3px;background:var(--green);margin:14px auto 0}
.beige{background:var(--beige)}
.more{display:block;width:200px;margin:0 auto;height:40px;border:1px solid var(--green);color:var(--green);text-align:center;line-height:38px;font-size:13px;text-decoration:none;background:#fff}

.strengths{height:640px}
.strength-grid{width:1080px;margin:34px auto 0;display:grid;grid-template-columns:repeat(3,340px);gap:50px 30px}
.strength-card{height:170px}
.strength-card .label{position:absolute;right:0;bottom:0;background:rgba(255,255,255,.92);padding:6px 14px;font-size:13px;display:flex;align-items:center;gap:8px}
.strength-card .label::before{content:"";width:10px;height:10px;border-radius:50%;background:var(--green);flex:none}

.service-row{width:1080px;margin:32px auto 0;display:grid;grid-template-columns:repeat(4,252px);gap:24px}
.tile{height:140px}
.tile .tag{position:absolute;left:0;right:0;bottom:0;background:rgba(31,139,59,.88);color:#fff;text-align:center;font-size:14px;line-height:30px}
.tile-text{font-size:12px;color:var(--muted);margin-top:12px;line-height:1.7}
.business{height:400px}
.products{height:428px}

/* news */
.news{height:224px;display:flex;background:var(--green)}
.news-head{width:380px;background:var(--green-deep);color:#fff;padding:56px 0 0 70px}
.news-head h2{font-family:"Noto Serif JP",serif;font-weight:500;font-size:30px;letter-spacing:.1em}
.news-head .more{margin:22px 0 0;width:160px;height:34px;line-height:32px;background:transparent;border-color:#fff;color:#fff}
.news-list{list-style:none;padding:36px 60px 0;flex:1;color:#fff}
.news-list li{display:flex;gap:28px;font-size:13px;line-height:38px;border-bottom:1px solid rgba(255,255,255,.3)}
.news-list .date{width:80px}
.news-list .cat{width:70px;opacity:.85}

/* blog */
.blog{height:448px}
.blog-grid{width:1080px;margin:24px auto 22px;display:grid;grid-template-columns:repeat(4,252px);gap:24px}
.blog-card .photo{height:130px}
.blog-card .date{font-size:11px;color:var(--muted);margin-top:6px;line-height:1.5}
.blog-card h3{font-size:14px;font-weight:700;margin:0 0 2px;line-height:1.5}
.blog-card p{font-size:12px;color:var(--muted);line-height:1.6}

/* faq */
.faq{height:640px}
.faq-list{width:880px;margin:30px auto 30px}
.faq-item{margin-bottom:18px}
.q,.a{display:flex;align-items:center;gap:14px;padding:8px 16px;font-size:15px;font-weight:700}
.q{background:#e4e1da}
.a{color:var(--brown);font-weight:500}
.badge{width:32px;height:32px;border-radius:50%;color:#fff;font-weight:700;display:flex;align-items:center;justify-content:center;flex:none;font-size:15px}
.q .badge{background:var(--green)}
.a .badge{background:var(--brown)}

/* footer */
.footer-nav{height:120px;padding-top:38px;text-align:center;font-size:12px;line-height:22px}
.footer-nav a{color:var(--ink);text-decoration:none;padding:0 6px}
.site-footer{height:256px;background:var(--beige);text-align:center;padding-top:44px}
.site-footer .brand{justify-content:center}
.address{font-size:12px;color:var(--muted);margin-top:10px}
.site-footer .contact-tel{justify-content:center;margin-top:6px}
.copyright{font-size:11px;color:var(--muted);margin-top:32px}
</style>
</head>
<body>
<header class="site-header">
  <div class="brand"><span class="brand-mark"></span>株式会社モリサト</div>
  <div class="contact">
    <p class="contact-note">お見積・お問い合わせはこちらまで</p>
    <p class="contact-tel"><svg width="22" height="22" viewBox="0 0 24 24"><path fill="#1f8b3b" d="M6.6 10.8a15.1 15.1 0 0 0 6.6 6.6l2.2-2.2c.3-.3.7-.4 1-.2 1.1.4 2.3.6 3.6.6.6 0 1 .4 1 1V20c0 .6-.4 1-1 1A17 17 0 0 1 3 4c0-.6.4-1 1-1h3.5c.6 0 1 .4 1 1 0 1.3.2 2.5.6 3.6.1.3 0 .7-.2 1z"/></svg>0276-00-4821</p>
  </div>
</header>
<nav class="global-nav">
  <a href="#">HOME</a><a href="#">弊社の強み</a><a href="#">事業案内</a><a href="#">加工事例・商品紹介</a><a href="#">会社案内</a><a href="#">よくある質問</a><a href="#" class="cta">お問い合わせ</a>
</nav>
<div class="hero photo" role="img" aria-label="木材をかんなで削る職人の手元と木くず"></div>

<section class="section strengths">
  <h2 class="section-title">弊社の強み</h2>
  <div class="strength-grid">
    <div class="strength-card photo light" role="img" aria-label="積み重ねた住宅部材"><span class="label">住宅部材加工</span></div>
    <div class="strength-card photo grey" role="img" aria-label="ショーケースの部材"><span class="label">建築機器(ショーケース)部材加工・組立</span></div>
    <div class="strength-card photo" role="img" aria-label="床張パネルの加工"><span class="label">床張パネル加工</span></div>
    <div class="strength-card photo light" role="img" aria-label="木製の梱包製品"><span class="label">梱包製品・梱包加工</span></div>
    <div class="strength-card photo grey" role="img" aria-label="加工治具と工場設備"><span class="label">その他・加工治具</span></div>
  </div>
</section>

<section class="section beige business">
  <h2 class="section-title">事業案内</h2>
  <div class="service-row">
    <div><div class="tile photo light" role="img" aria-label="積まれた木材"><span class="tag">木材</span></div><p class="tile-text">テキストテキストテキストテキストテキストテキストテキストテキスト</p></div>
    <div><div class="tile photo" role="img" aria-label="加工された集成材"><span class="tag">加工・組立</span></div><p class="tile-text">テキストテキストテキストテキストテキストテキストテキストテキスト</p></div>
    <div><div class="tile photo grey" role="img" aria-label="工場の加工設備"><span class="tag">設備</span></div><p class="tile-text">テキストテキストテキストテキストテキストテキストテキストテキスト</p></div>
    <div><div class="tile photo green" role="img" aria-label="屋外の木製あずまや"><span class="tag">オーダーメイド</span></div><p class="tile-text">テキストテキストテキストテキストテキストテキストテキストテキスト</p></div>
  </div>
</section>

<section class="section products">
  <h2 class="section-title">加工事例・商品紹介</h2>
  <div class="service-row">
    <div><div class="tile photo green" role="img" aria-label="木製の案内板"><span class="tag">案内板</span></div><p class="tile-text">テキストテキストテキストテキストテキストテキストテキストテキスト</p></div>
    <div><div class="tile photo" role="img" aria-label="木製の看板"><span class="tag">看板</span></div><p class="tile-text">テキストテキストテキストテキストテキストテキストテキストテキスト</p></div>
    <div><div class="tile photo green" role="img" aria-label="屋外の木製ブランコ"><span class="tag">ブランコ</span></div><p class="tile-text">テキストテキストテキストテキストテキストテキストテキストテキスト</p></div>
    <div><div class="tile photo green" role="img" aria-label="芝生に置かれた木製スタンド"><span class="tag">キャンドスタンド</span></div><p class="tile-text">テキストテキストテキストテキストテキストテキストテキストテキスト</p></div>
  </div>
</section>

<section class="news">
  <div class="news-head">
    <h2>ニュース</h2>
    <a href="#" class="more">一覧を見る</a>
  </div>
  <ul class="news-list">
    <li><span class="date">2019.1.1</span><span class="cat">お知らせ</span><span>テキストテキストテキストテキストテキストテキストテキスト</span></li>
    <li><span class="date">2019.1.1</span><span class="cat">お知らせ</span><span>テキストテキストテキストテキストテキストテキストテキスト</span></li>
    <li><span class="date">2019.1.1</span><span class="cat">お知らせ</span><span>テキストテキストテキストテキストテキストテキストテキスト</span></li>
    <li><span class="date">2019.1.1</span><span class="cat">お知らせ</span><span>テキストテキストテキストテキストテキストテキストテキスト</span></li>
  </ul>
</section>

<section class="section blog">
  <h2 class="section-title">ブログ</h2>
  <div class="blog-grid">
    <article class="blog-card"><div class="photo" role="img" aria-label="木工作業の様子"></div><p class="date">2019.1.1</p><h3>タイトルタイトルタイトル</h3><p>テキストテキストテキストテキストテキストテキスト…続きを読む</p></article>
    <article class="blog-card"><div class="photo light" role="img" aria-label="木材を加工する手元"></div><p class="date">2019.1.1</p><h3>タイトルタイトルタイトル</h3><p>テキストテキストテキストテキストテキストテキスト…続きを読む</p></article>
    <article class="blog-card"><div class="photo" role="img" aria-label="工具と木材"></div><p class="date">2019.1.1</p><h3>タイトルタイトルタイトル</h3><p>テキストテキストテキストテキストテキストテキスト…続きを読む</p></article>
    <article class="blog-card"><div class="photo light" role="img" aria-label="並べられた木材"></div><p class="date">2019.1.1</p><h3>タイトルタイトルタイトル</h3><p>テキストテキストテキストテキストテキストテキスト…続きを読む</p></article>
  </div>
  <a href="#" class="more">一覧を見る</a>
</section>

<section class="section beige faq">
  <h2 class="section-title">よくある質問</h2>
  <div class="faq-list">
    <div class="faq-item"><p class="q"><span class="badge">Q</span>テキストテキストテキストテキストテキストテキストテキストテキストテキスト</p><p class="a"><span class="badge">A</span>テキストテキストテキストテキストテキストテキストテキストテキストテキスト</p></div>
    <div class="faq-item"><p class="q"><span class="badge">Q</span>テキストテキストテキストテキストテキストテキストテキストテキストテキスト</p><p class="a"><span class="badge">A</span>テキストテキストテキストテキストテキストテキストテキストテキストテキスト</p></div>
    <div class="faq-item"><p class="q"><span class="badge">Q</span>テキストテキストテキストテキストテキストテキストテキストテキストテキスト</p><p class="a"><span class="badge">A</span>テキストテキストテキストテキストテキストテキストテキストテキストテキスト</p></div>
  </div>
  <a href="#" class="more">一覧を見る</a>
</section>

<nav class="footer-nav">
  <p><a href="#">HOME</a>|<a href="#">弊社の強み</a>|<a href="#">事業案内</a>|<a href="#">加工事例・商品紹介</a>|<a href="#">会社案内</a>|<a href="#">よくある質問</a>|<a href="#">採用情報</a></p>
  <p><a href="#">お問い合わせ</a>|<a href="#">プライバシーポリシー</a>|<a href="#">サイトマップ</a></p>
</nav>
<footer class="site-footer">
  <div class="brand"><span class="brand-mark"></span>株式会社モリサト</div>
  <p class="address">〒370-0000 群馬県○○市○○町1-2-3</p>
  <p class="contact-tel"><svg width="22" height="22" viewBox="0 0 24 24"><path fill="#1f8b3b" d="M6.6 10.8a15.1 15.1 0 0 0 6.6 6.6l2.2-2.2c.3-.3.7-.4 1-.2 1.1.4 2.3.6 3.6.6.6 0 1 .4 1 1V20c0 .6-.4 1-1 1A17 17 0 0 1 3 4c0-.6.4-1 1-1h3.5c.6 0 1 .4 1 1 0 1.3.2 2.5.6 3.6.1.3 0 .7-.2 1z"/></svg>0276-00-4821</p>
  <p class="copyright">Copyright © 2019 株式会社モリサト All Right Reserved.</p>
</footer>
</body>
</html>
```